Deal Email Template Design

I need a number of email templates designed for my deal website. The emails will be used to promote, market, and sell it's deals. Emails will be launched using an email marketing platform. I will work with chosen designer to detail the company description, branding, logos, etc.
Updates
Reason: I added details to project and would like to see some more bids. Please feel free to submit and ask any questions.
Thank you.
Target Market(s)
Casino Destination Travelers
Industry/Entity Type
It Company
Look and feel
Each slider illustrates characteristics of the customer's brand and the style your logo design should communicate.

```html
<!DOCTYPE html>
<html lang="en">
<head>
<meta charset="utf-8">
<title>Deal Email Template</title>
<link rel="stylesheet" href="https://fonts.googleapis.com/css2?family=Open+Sans:wght@300;400;600&display=swap">
<style>
:root{
  --bg:#131313;
  --card:#1b1b1b;
  --cell:#1e1e1e;
  --divider:#2c2c2c;
  --text:#8c8c8c;
  --title:#c9c9c9;
  --icon:#7a7a7a;
  --accent:#e8c31e;
  --timeline:#3a3a3a;
}
*{box-sizing:border-box;margin:0;padding:0}
html,body{width:894px;height:1200px;overflow:hidden;background:var(--bg)}
body{position:relative;font-family:"Open Sans",sans-serif;color:var(--text)}
.timeline{position:absolute;left:37px;top:0;width:2px;height:1200px;background:var(--timeline)}
.timeline-dot{position:absolute;left:31px;width:14px;height:14px;border:2px solid #555;border-radius:50%;background:var(--bg)}
.timeline-dot::after{content:"";position:absolute;left:3px;top:3px;width:4px;height:4px;border-radius:50%;background:#666}
.footer-rule{position:absolute;left:0;top:1112px;width:894px;height:2px;background:#262626}
.footer{position:absolute;right:73px;top:1122px;font-size:11px;color:#8a8a8a}
.hero-photo{position:absolute;left:98px;top:40px;width:727px;height:248px;
  background:linear-gradient(100deg,#2a2f5a 0%,#8a3a28 35%,#5a2a18 60%,#b07a55 85%,#d9b08c 100%)}
.action-bar{position:absolute;left:98px;width:727px;height:53px;display:flex;gap:2px;background:var(--bg)}
.action-bar .cell{background:var(--cell);display:flex;flex-direction:column;align-items:center;justify-content:center;font-size:14px;color:var(--icon)}
.cell.brand-slot{width:133px}
.cell.post-title{width:166px;font-size:19px;font-weight:300;color:var(--title)}
.cell.like{width:121px}
.cell.share{width:143px}
.cell.comment{flex:1}
.cell.comment.active{background:var(--accent);color:#fff}
.cell svg{width:24px;height:20px;margin-bottom:1px}
.badge{position:absolute;left:119px;width:94px;height:94px;border-radius:50%;border:3px solid var(--accent);background:#3b3b3b;
  display:flex;align-items:center;justify-content:center;font-size:14px;font-weight:600;color:var(--accent)}
.badge.photo{background:radial-gradient(circle at 40% 40%,#4a5a8a,#2a1a14 70%)}
.tweet-card{position:absolute;left:98px;top:367px;width:727px;height:252px;background:var(--card)}
.tweet-source{position:absolute;left:30px;top:64px;width:74px;text-align:center;font-size:14px;font-weight:600;color:var(--accent)}
.tweet-text{position:absolute;left:135px;top:24px;width:560px;font-size:15.5px;font-weight:300;line-height:23px}
.story{position:absolute;background:var(--card)}
.story h2{height:47px;padding:0 16px;display:flex;align-items:center;font-size:19px;font-weight:300;color:var(--title);border-bottom:1px solid var(--divider)}
.story p{font-size:14px;font-weight:300;line-height:18px}
.story.left{left:98px;top:653px;width:356px;height:395px}
.story.left .story-photo{margin-top:2px;height:193px;background:linear-gradient(90deg,#2b2f2c 0%,#6a4a38 35%,#b02a2a 70%,#3a2525 100%)}
.story.left p{padding:20px 20px 0 20px}
.story.right-top{left:468px;top:654px;width:356px;height:189px}
.story.right-top p{padding:7px 20px 0 20px}
.story.right-bottom{left:468px;top:859px;width:356px;height:189px}
.story.right-bottom .thumb{position:absolute;left:22px;top:55px;width:118px;height:118px;border:2px solid #bbb;
  background:linear-gradient(135deg,#a02a4a 0%,#2a5a3a 55%,#1a1a1a 100%)}
.story.right-bottom p{position:absolute;left:158px;top:57px;width:185px}
</style>
</head>
<body>
<div class="timeline"></div>
<div class="timeline-dot" style="top:64px"></div>
<div class="timeline-dot" style="top:394px"></div>
<div class="timeline-dot" style="top:679px"></div>
<div class="timeline-dot" style="top:1105px"></div>

<div class="hero-photo" role="img" aria-label="Row of slot machines with players in a casino"></div>
<div class="action-bar" style="top:289px">
  <div class="cell brand-slot"></div>
  <div class="cell post-title">Add title here</div>
  <div class="cell like"><svg viewBox="0 0 24 20"><path d="M12 19 2.5 10A5 5 0 0 1 12 4a5 5 0 0 1 9.5 6Z" fill="currentColor"/></svg>like</div>
  <div class="cell share"><svg viewBox="0 0 24 20"><path d="M14 2l8 7-8 7v-4c-6 0-9 2-12 6 1-7 5-11 12-11Z" fill="currentColor"/></svg>share</div>
  <div class="cell comment active"><svg viewBox="0 0 24 20"><path d="M3 2h13a2 2 0 0 1 2 2v6a2 2 0 0 1-2 2H9l-5 4v-4H3a2 2 0 0 1-2-2V4a2 2 0 0 1 2-2Z" fill="currentColor"/><path d="M20 6h1a2 2 0 0 1 2 2v6a2 2 0 0 1-2 2h-1v3l-4-3h-5" fill="none" stroke="currentColor" stroke-width="2"/></svg>comment</div>
</div>
<div class="badge" style="top:239px">Luckdeal</div>

<div class="tweet-card">
  <div class="tweet-source">Chirpline</div>
  <p class="tweet-text">Lorem ipsum dolor sit amet, consectetur adipiscing elit. Mauris id hendrerit enim. Aenean tempor, dolor at imperdiet molestie, arcu mauris bibendum mauris, et placerat nulla elit ut leo. Duis ultricies auctor massa, vel varius felis porta vitae. Sed hendrerit tristique cursus. Nullam faucibus feugiat nisl eget facilisis. Quisque id dolor vestibulum sapien vestibulum egestas id eget nisl. Nunc laoreet venenatis placerat.</p>
</div>
<div class="action-bar" style="top:567px">
  <div class="cell brand-slot"></div>
  <div class="cell post-title">Add title here</div>
  <div class="cell like"><svg viewBox="0 0 24 20"><path d="M12 19 2.5 10A5 5 0 0 1 12 4a5 5 0 0 1 9.5 6Z" fill="currentColor"/></svg>like</div>
  <div class="cell share"><svg viewBox="0 0 24 20"><path d="M14 2l8 7-8 7v-4c-6 0-9 2-12 6 1-7 5-11 12-11Z" fill="currentColor"/></svg>share</div>
  <div class="cell comment"><svg viewBox="0 0 24 20"><path d="M3 2h13a2 2 0 0 1 2 2v6a2 2 0 0 1-2 2H9l-5 4v-4H3a2 2 0 0 1-2-2V4a2 2 0 0 1 2-2Z" fill="currentColor"/><path d="M20 6h1a2 2 0 0 1 2 2v6a2 2 0 0 1-2 2h-1v3l-4-3h-5" fill="none" stroke="currentColor" stroke-width="2"/></svg>comment</div>
</div>
<div class="badge photo" style="top:517px" role="img" aria-label="Player at a slot machine"></div>

<article class="story left">
  <h2>Add title for the substory here</h2>
  <div class="story-photo" role="img" aria-label="Group of friends cheering at a roulette table"></div>
  <p>Lorem ipsum dolor sit amet, consectetur adipi-scing elit. Mauris id hendrerit enim. Aenean tempor, dolor at imperdiet molestie, arcu mauris bibendum mauris, et placerat nulla elit ut leo. Duis ultricies auctor massa, vel varius felis porta vitae. Sed hendrerit tristique cursus. Nullam faucibus feugiat nisl eget facilisis.</p>
</article>

<article class="story right-top">
  <h2>Add title for the substory here</h2>
  <p>Lorem ipsum dolor sit amet, consectetur adipi-scing elit. Mauris id hendrerit enim. Aenean tempor, dolor at imperdiet molestie, arcu mauris bibendum mauris, et placerat nulla elit ut leo. Duis ultricies auctor massa, vel varius felis porta vitae. Sed hendrerit tristique cursus. Nullam faucibus feugiat nisl eget facilisis.</p>
</article>

<article class="story right-bottom">
  <h2>Add title for the substory here</h2>
  <div class="thumb" role="img" aria-label="Stacks of casino chips"></div>
  <p>Lorem ipsum dolor sit amet, consectetur adipi-scing elit. Mauris id hen-drerit enim. Aenean tempor, dolor at imperdiet molestie, arcu mauris bibendum mauris.</p>
</article>

<div class="footer-rule"></div>
<footer class="footer">Footer text and links come here - First link - Second link - And so on</footer>
</body>
</html>
```